Visit card

Industry/Entity Type

Health Care

Contact Information for Business Card

O VITAL SYSTEMIQUE
Odile Ferrand - chef de Projet

Requirements
Must have
• 318 Rue des Tilleuls Verts 47150 BÉTHUNE Tel: 33 (0) 487 204 615 Mobile: 06 42 93 17 58 Web: www.cliniqorvane.example Contact: o.ferrand@o-vitalsystemique.example
Should not have
• Respect for color

```html
<!DOCTYPE html>
<html lang="fr">
<head>
<meta charset="utf-8">
<title>O Vital Systemique – Carte de visite</title>
<link href="https://fonts.googleapis.com/css2?family=Lato:wght@400;700&display=swap" rel="stylesheet">
<style>
  :root {
    --backdrop: #e9e4dd;
    --card: #f3f1ee;
    --card-edge: #d9d4cd;
    --red: #d0262e;
    --charcoal: #3b3a3a;
    --ink: #555453;
  }
  * { margin: 0; padding: 0; box-sizing: border-box; }
  html, body {
    width: 1200px;
    height: 1047px;
    overflow: hidden;
    background: var(--backdrop);
    font-family: "Lato", sans-serif;
  }
  .business-card {
    position: absolute;
    left: 120px;
    top: 263px;
    width: 960px;
    height: 520px;
    background: var(--card);
    border: 1px solid var(--card-edge);
    border-radius: 18px;
    box-shadow: 0 10px 30px rgba(0,0,0,0.08);
  }
  .brand {
    position: absolute;
    left: 36px;
    top: 34px;
    display: flex;
    align-items: center;
    gap: 22px;
  }
  .brand-dot {
    width: 104px;
    height: 104px;
    border-radius: 50%;
    background: var(--charcoal);
  }
  .brand-name {
    font-weight: 700;
    font-size: 30px;
    letter-spacing: 1px;
    color: var(--red);
  }
  .holder {
    position: absolute;
    left: 36px;
    top: 166px;
  }
  .holder-name {
    font-size: 30px;
    font-weight: 400;
    letter-spacing: 0.5px;
    color: var(--red);
    text-transform: uppercase;
    line-height: 1.1;
  }
  .holder-role {
    font-size: 20px;
    color: var(--ink);
    margin-top: 6px;
  }
  .address {
    position: absolute;
    left: 36px;
    top: 274px;
    font-size: 20px;
    color: var(--ink);
    line-height: 31px;
    font-style: normal;
  }
  .contacts {
    position: absolute;
    left: 36px;
    top: 365px;
    list-style: none;
    font-size: 20px;
    color: var(--ink);
  }
  .contacts li {
    display: flex;
    align-items: center;
    height: 31px;
    gap: 10px;
  }
  .contacts svg {
    width: 14px;
    height: 14px;
    fill: none;
    stroke: var(--red);
    stroke-width: 2;
  }
  .emblem {
    position: absolute;
    left: 445px;
    top: 24px;
    width: 470px;
    height: 470px;
  }
</style>
</head>
<body>
  <main class="business-card">
    <div class="brand">
      <span class="brand-dot"></span>
      <span class="brand-name">O VITAL SYSTEMIQUE</span>
    </div>

    <div class="holder">
      <h1 class="holder-name">Odile Ferrand</h1>
      <p class="holder-role">Chef de Projet</p>
    </div>

    <address class="address">
      318 Rue des Tilleuls Verts<br>
      47150 BÉTHUNE
    </address>

    <ul class="contacts">
      <li>
        <svg viewBox="0 0 14 14"><path d="M3 1 L5.5 3.5 L4 5.5 Q6 8.5 8.5 10 L10.5 8.5 L13 11 L11 13 Q5 12 1 3 Z" fill="var(--red)" stroke="none"/></svg>
        +33 (0) 487 204 615
      </li>
      <li>
        <svg viewBox="0 0 14 14"><rect x="3.5" y="1" width="7" height="12" rx="1.2"/><line x1="6" y1="10.5" x2="8" y2="10.5"/></svg>
        06 42 93 17 58
      </li>
      <li>
        <svg viewBox="0 0 14 14" style="stroke-width:1.3"><circle cx="7" cy="7" r="5.8"/><ellipse cx="7" cy="7" rx="2.5" ry="5.8"/><line x1="1.2" y1="7" x2="12.8" y2="7"/></svg>
        www.cliniqorvane.example
      </li>
      <li>
        <svg viewBox="0 0 14 14" style="stroke-width:1.4"><rect x="1" y="3" width="12" height="8.5" rx="0.8"/><path d="M1.5 3.5 L7 8 L12.5 3.5"/></svg>
        o.ferrand@o-vitalsystemique.example
      </li>
    </ul>

    <svg class="emblem" viewBox="0 0 470 470" aria-hidden="true">
      <circle cx="235" cy="235" r="210" fill="none" stroke="var(--charcoal)" stroke-width="46"/>
    </svg>
  </main>
</body>
</html>
```